Pelin Thai Massage Double Sided Flyer Luxury

I require a double sided flyer
we are a Thai Massage Spa
Would like gold, deep purple and bronze colours
Something eye catching and looks professional

```html
<!DOCTYPE html>
<html lang="en">
<head>
<meta charset="utf-8">
<title>Pelin Thai Massage – Double Sided Flyer</title>
<link href="https://fonts.googleapis.com/css2?family=Abril+Fatface&family=Playfair+Display:wght@400;700;900&family=Montserrat:wght@400;600;700&family=Oswald:wght@300&display=swap" rel="stylesheet">
<style>
  :root {
    --bg: #e6e6e6;
    --gold: #d9a93a;
    --gold-light: #f6d365;
    --gold-dark: #b8862a;
    --bronze: #a65430;
    --bronze-light: #cf8458;
    --bronze-dark: #7a3a1e;
    --ink: #000000;
    --paper: #ffffff;
  }
  * { box-sizing: border-box; margin: 0; padding: 0; }
  html, body { width: 1200px; height: 864px; overflow: hidden; }
  body { background: var(--bg); position: relative; font-family: "Playfair Display", serif; }

  .flyer {
    position: absolute; top: 105px; width: 505px; height: 653px;
    background: linear-gradient(135deg, var(--gold-dark), var(--gold-light) 30%, var(--gold) 55%, var(--gold-light) 80%, var(--gold-dark));
    box-shadow: 0 10px 28px rgba(0,0,0,.35);
  }
  .flyer--front { left: 77px; }
  .flyer--back { left: 618px; }

  .flyer__inner {
    position: absolute; left: 16px; top: 16px; width: 474px; height: 622px;
    background: linear-gradient(135deg, var(--bronze-dark), var(--bronze-light) 35%, var(--bronze) 60%, var(--bronze-light) 85%, var(--bronze-dark));
  }
  .photo { position: absolute; left: 0; top: 0; width: 474px; }
  .photo--back-massage { height: 308px; background: linear-gradient(120deg, #f3ece4 0%, #e9c9a6 35%, #a8582e 65%, #3a2418 100%); }
  .photo--face-massage { height: 229px; background: linear-gradient(100deg, #f4eee8 0%, #ecd0b6 40%, #e6c9ad 60%, #9a6a3c 85%, #3b2a1e 100%); }

  .panel { position: absolute; left: 19px; width: 434px; background: var(--ink); color: var(--paper); }
  .panel--welcome { top: 325px; height: 176px; border-radius: 22px 0 0 0; border-bottom-right-radius: 22px; text-align: center; padding: 10px 22px 0; }
  .panel--contact { top: 512px; height: 92px; border-radius: 16px 0 0 16px; border-top-right-radius: 16px; display: flex; align-items: center; }

  .welcome__title {
    font-family: "Abril Fatface", serif; font-weight: 400; font-size: 37px; line-height: 1.1;
    color: var(--gold); letter-spacing: .5px; white-space: nowrap;
  }
  .divider { display: flex; align-items: center; justify-content: center; gap: 10px; margin: 4px 0 8px; }
  .divider__line { width: 154px; height: 1px; background: var(--paper); opacity: .8; }
  .divider__dot { width: 12px; height: 12px; border: 1.5px solid var(--gold); border-radius: 50%; }
  .welcome__text { font-size: 10px; line-height: 1.35; margin-bottom: 6px; }

  .contact__list { list-style: none; padding-left: 24px; width: 255px; font-family: "Montserrat", sans-serif; font-size: 12px; color: var(--gold); }
  .contact__list li { display: flex; align-items: center; gap: 10px; margin: 7px 0; white-space: nowrap; }
  .contact__list b { font-weight: 600; }
  .icon { width: 14px; height: 14px; flex: none; }
  .contact__rule { width: 1px; height: 64px; background: var(--gold); opacity: .7; }
  .brand { flex: 1; display: flex; flex-direction: column; align-items: center; gap: 8px; }
  .brand__dot { width: 30px; height: 30px; border-radius: 50%; background: var(--gold); }
  .brand__name { font-family: "Montserrat", sans-serif; font-size: 11px; color: var(--gold); }

  .panel--menu { top: 251px; height: 280px; border-radius: 22px 0 0 0; border-bottom-right-radius: 22px; text-align: center; padding-top: 14px; }
  .menu__heading { display: flex; align-items: center; justify-content: center; gap: 18px; height: 28px; }
  .menu__heading .divider__line { width: 100px; }
  .menu__title { font-family: "Playfair Display", serif; font-weight: 900; font-size: 24px; line-height: 28px; color: var(--gold); letter-spacing: .5px; }
  .menu__intro { font-size: 10px; line-height: 13px; margin: 6px 28px 0; }
  .pill {
    display: inline-block; border-radius: 13px; height: 26px; line-height: 26px; white-space: nowrap;
    background: linear-gradient(90deg, var(--gold-dark), var(--gold-light) 50%, var(--gold-dark));
    font-family: "Playfair Display", serif; font-weight: 700; font-size: 14px; color: #1a1204;
  }
  .pill--deep { width: 209px; margin-top: 9px; }
  .pill--thai { width: 307px; margin-top: 15px; }
  .prices { display: flex; justify-content: center; gap: 12px; margin-top: 10px; }
  .prices--thai { margin-top: 11px; }
  .price {
    display: flex; height: 51px; border: 1px solid var(--gold); border-radius: 0 6px 6px 0; text-align: left;
  }
  .price__info { width: 117px; padding: 6px 0 0 12px; }
  .price--wide .price__info { width: 197px; padding-left: 16px; }
  .price__time { font-family: "Montserrat", sans-serif; font-weight: 700; font-size: 13px; }
  .price__note { font-size: 8px; line-height: 1.3; margin-top: 1px; }
  .price__amount {
    width: 64px; border-left: 1px solid var(--gold); display: flex; align-items: center; justify-content: center;
    font-family: "Montserrat", sans-serif; font-weight: 700; font-size: 25px;
  }
  .price--wide .price__amount { width: 71px; }

  .banner {
    position: absolute; left: 19px; top: 531px; width: 434px; height: 39px;
    background: linear-gradient(90deg, var(--gold-dark), var(--gold-light) 50%, var(--gold-dark));
    border-bottom-right-radius: 22px;
    display: flex; align-items: center; justify-content: center; gap: 10px;
    font-family: "Oswald", sans-serif; font-weight: 300; font-size: 22px; color: #1a1204; letter-spacing: .2px; white-space: nowrap;
  }
  .contact-strip {
    position: absolute; left: 19px; top: 584px; width: 434px; height: 25px;
    background: rgba(122,58,30,.55);
    display: flex; align-items: center; justify-content: space-around;
    font-family: "Montserrat", sans-serif; font-size: 11px; color: var(--paper); white-space: nowrap;
  }
  .contact-strip__item { display: flex; align-items: center; gap: 5px; }
  .contact-strip b { font-weight: 600; }
  .contact-strip .icon { width: 11px; height: 11px; }
</style>
</head>
<body>

<svg width="0" height="0" style="position:absolute">
  <defs>
    <symbol id="icon-phone" viewBox="0 0 16 16"><circle cx="8" cy="8" r="7" fill="none" stroke="currentColor" stroke-width="1.2"/><path d="M5.5 4.5l1.5 0 .6 2-1 .8a5 5 0 0 0 2.1 2.1l.8-1 2 .6v1.5c-3.8.3-6.3-2.2-6-6z" fill="none" stroke="currentColor" stroke-width="1"/></symbol>
    <symbol id="icon-mail" viewBox="0 0 16 16"><circle cx="8" cy="8" r="7" fill="none" stroke="currentColor" stroke-width="1.2"/><rect x="4.5" y="5.5" width="7" height="5" fill="none" stroke="currentColor" stroke-width="1"/><path d="M4.5 5.5L8 8.5l3.5-3" fill="none" stroke="currentColor" stroke-width="1"/></symbol>
    <symbol id="icon-globe" viewBox="0 0 16 16"><circle cx="8" cy="8" r="7" fill="none" stroke="currentColor" stroke-width="1.2"/><circle cx="8" cy="8" r="4" fill="none" stroke="currentColor" stroke-width="1"/><path d="M4 8h8M8 4c-1.5 2.5-1.5 5.5 0 8M8 4c1.5 2.5 1.5 5.5 0 8" fill="none" stroke="currentColor" stroke-width=".9"/></symbol>
  </defs>
</svg>

<section class="flyer flyer--front" role="img" aria-label="Gold border with ornate damask pattern">
  <div class="flyer__inner" role="img" aria-label="Bronze damask ornamental background">
    <div class="photo photo--back-massage" role="img" aria-label="Photo of a woman receiving a back massage beside a lit candle"></div>

    <div class="panel panel--welcome">
      <h1 class="welcome__title">Welcome to Luxury</h1>
      <div class="divider"><span class="divider__line"></span><span class="divider__dot"></span><span class="divider__line"></span></div>
      <p class="welcome__text">Set in the heart of Elmwood Park, Pelin Thai Massage will allow you to immerse yourself in a place where your wellbeing and rejuvenation is at the centre of what we do.</p>
      <p class="welcome__text">Using Thai traditions, our highly trained therapists offer revitalising body treatments with their deep tissue massage techniques. In their hands, you will see and feel immediate results.</p>
    </div>

    <div class="panel panel--contact">
      <ul class="contact__list">
        <li><svg class="icon"><use href="#icon-phone"/></svg><span>0113 496 0721</span></li>
        <li><svg class="icon"><use href="#icon-mail"/></svg><span>www.<b>PelinThaiMassage</b>.co.uk</span></li>
        <li><svg class="icon"><use href="#icon-globe"/></svg><span>hello@pelinthai.co.uk</span></li>
      </ul>
      <span class="contact__rule"></span>
      <div class="brand">
        <span class="brand__dot"></span>
        <span class="brand__name">Pelin Thai Massage</span>
      </div>
    </div>
  </div>
</section>

<section class="flyer flyer--back" role="img" aria-label="Gold border with ornate damask pattern">
  <div class="flyer__inner" role="img" aria-label="Bronze damask ornamental background">
    <div class="photo photo--face-massage" role="img" aria-label="Photo of a woman receiving a head massage beside spa accessories on a bamboo mat"></div>

    <div class="panel panel--menu">
      <div class="menu__heading"><span class="divider__line"></span><h2 class="menu__title">MASSAGES</h2><span class="divider__line"></span></div>
      <p class="menu__intro">Restore balance. Revive your senses. Discover all the ways Pelin Thai Massage can breathe new life into your body and soul.</p>

      <div class="pill pill--deep">DEEP TISSUE MASSAGE</div>
      <div class="prices">
        <div class="price">
          <div class="price__info"><div class="price__time">60 minutes</div><div class="price__note">Oil massage personalised, light to firm pressure</div></div>
          <div class="price__amount">£45</div>
        </div>
        <div class="price">
          <div class="price__info"><div class="price__time">90 minutes</div><div class="price__note">Oil massage, medium to firm pressure</div></div>
          <div class="price__amount">£55</div>
        </div>
      </div>

      <div class="pill pill--thai">THAI FLOOR TRADTIONAL MASSAGE</div>
      <div class="prices prices--thai">
        <div class="price price--wide">
          <div class="price__info"><div class="price__time">60 minutes</div><div class="price__note">Dry massage, medium to firm pressure applying stretching technique</div></div>
          <div class="price__amount">£45</div>
        </div>
      </div>
    </div>

    <div class="banner"><span>GIFT VOUCHERS AVAILABLE</span><span>|</span><span>OPEN 7 DAYS A WEEK</span></div>

    <div class="contact-strip">
      <span class="contact-strip__item"><svg class="icon"><use href="#icon-phone"/></svg><span>0113 496 0721</span></span>
      <span class="contact-strip__item"><svg class="icon"><use href="#icon-globe"/></svg><span>www.<b>PelinThaiMassage</b>.co.uk</span></span>
      <span class="contact-strip__item"><svg class="icon"><use href="#icon-mail"/></svg><span>hello@pelinthai.co.uk</span></span>
    </div>
  </div>
</section>

</body>
</html>
```